Refresh of Medical Website

We are wanting to revamp our website and add much more content to the site. Our current website is https://corvalepracticehub.com.au/. We also want someone to be able to upload this to our server.

Target Market(s)

Medical

Coding

Coded - Design and coding required

Number of Pages Required

5+ page

Font styles to use
Sans Serif

Colors
85cae6
ecf7fb
fafcfe
3176b5

Requirements
Must have
• I will pride a document of all inspiration and additions we would like please contact me and I will provide this.

```html
<!DOCTYPE html>
<html lang="en">
<head>
<meta charset="utf-8">
<title>Corvale ENT Victoria</title>
<link href="https://fonts.googleapis.com/css2?family=Roboto:wght@300;400;500;700&display=swap" rel="stylesheet">
<style>
:root{
  --navy:#1f3a6e;
  --navy-deep:#223052;
  --footer:#25304d;
  --footer-bar:#1d2640;
  --magenta:#982a78;
  --slate:#4d4e52;
  --ink:#1b1b1b;
  --grey-bg:#f1f1f1;
  --line:#e3e3e3;
  --white:#fff;
  --loc-text:#5a74a8;
}
*{box-sizing:border-box;margin:0;padding:0}
html,body{width:1200px;height:3754px;overflow:hidden;background:var(--white);font-family:'Roboto',Arial,sans-serif;color:var(--ink)}
.page{position:relative;width:1200px;height:3754px;overflow:hidden}
.abs{position:absolute}
/* header */
.header{left:0;top:0;width:1200px;height:108px;border-bottom:2px solid #d8dfea;background:var(--white)}
.brand{display:flex;align-items:center;gap:12px;left:26px;top:34px}
.brand-dot{width:40px;height:40px;border-radius:50%;background:var(--navy)}
.brand-name{font-size:27px;font-weight:400;color:var(--navy);letter-spacing:-.3px}
.topbar{right:230px;top:34px;display:flex;align-items:center;gap:10px;font-size:13px;font-weight:500;color:#222}
.topbar .soc{width:10px;height:10px;background:#222;border-radius:2px}
.topbar .sep{color:#666}
.btn-book{left:968px;top:18px;width:192px;height:48px;background:var(--navy);color:#fff;font-size:13px;font-weight:700;display:flex;align-items:center;justify-content:center;box-shadow:0 2px 4px rgba(0,0,0,.25)}
.nav{right:40px;top:78px;display:flex;gap:24px;font-size:14px;color:#333}
/* hero */
.hero{left:0;top:110px;width:1200px;height:602px;background:linear-gradient(100deg,#2e4776 0%,#4d6793 35%,#8aa6c6 60%,#b9cadb 100%)}
.hero-shade{left:0;top:110px;width:1200px;height:602px;background:linear-gradient(90deg,rgba(22,36,70,.6),rgba(22,36,70,0) 60%)}
.hero h1{left:109px;top:312px;font-size:33px;font-weight:500;color:#fff}
.hero-sub{left:110px;top:364px;font-size:23px;line-height:30px;font-weight:500;color:#fff}
.btn-pill{background:#fff;color:var(--navy);border-radius:26px;font-size:14px;font-weight:700;display:flex;align-items:center;justify-content:center}
.hero-cta{left:112px;top:452px;width:144px;height:47px}
.arrow{width:37px;height:37px;border-radius:50%;background:#fff;top:392px;display:flex;align-items:center;justify-content:center}
/* feature cards */
.feature{top:645px;width:300px;height:181px;color:#fff;text-align:center;box-shadow:0 3px 8px rgba(0,0,0,.2)}
.feature h3{margin-top:36px;font-size:20px;font-weight:700}
.feature .rule{width:62px;height:2px;background:#fff;margin:8px auto 0}
.feature .btn-pill{width:140px;height:46px;margin:22px auto 0}
.f-book{left:111px;background:var(--navy)}
.f-clinic{left:450px;background:var(--slate)}
.f-team{left:789px;background:var(--magenta)}
.f-clinic .btn-pill{color:var(--slate)}
.f-team .btn-pill{color:var(--magenta)}
/* services */
.services-bg{left:0;top:712px;width:1200px;height:812px;background:var(--grey-bg);z-index:-1}
.tile{width:317px;height:244px;background:#fff;border:1px solid var(--line);box-shadow:0 1px 3px rgba(0,0,0,.08)}
.tile .ph{position:absolute;left:6px;top:6px;width:305px;height:184px}
.tile span{position:absolute;left:0;right:0;top:205px;text-align:center;font-size:20px;font-weight:700;color:#111}
/* about */
.about-photo{left:500px;top:1524px;width:700px;height:475px;background:linear-gradient(120deg,#8ea3bf,#c7d2de 50%,#e5e9ee)}
.about h2{left:117px;top:1600px;font-size:34px;font-weight:700;color:#fff}
.about .rule{left:119px;top:1648px;width:74px;height:2px;background:#fff}
.about p{left:119px;top:1668px;width:420px;font-size:13.5px;line-height:26.5px;color:#fff;text-align:justify}
.btn-outline{left:118px;top:1866px;width:152px;height:46px;border:2px solid #fff;border-radius:24px;color:#fff;font-size:15px;font-weight:500;display:flex;align-items:center;justify-content:center}
/* appointment */
.sec-title{left:0;width:1200px;text-align:center;font-size:34px;font-weight:700;color:#111}
.sec-rule{left:568px;width:64px;height:3px;background:var(--navy)}
.intro{left:0;top:2160px;width:1200px;text-align:center;font-size:15px;line-height:26px;font-weight:500;color:#222}
.need{top:2236px;width:240px;height:249px;background:#fff;box-shadow:0 2px 10px rgba(0,0,0,.1);border-radius:4px;text-align:center}
.need .ring{width:106px;height:106px;border:1.5px solid #c9c9c9;border-radius:50%;margin:19px auto 0;display:flex;align-items:center;justify-content:center}
.need p{margin-top:18px;font-size:14.5px;line-height:23px;font-weight:500;padding:0 16px}
/* locations */
.loc-bg{left:0;top:2616px;width:1200px;height:629px;background:linear-gradient(180deg,#f3f4f6 0%,#e6e9ee 60%,#c9d0da 100%)}
.loc{top:2792px;width:235px;height:341px;background:#fff;box-shadow:0 1px 4px rgba(0,0,0,.15);text-align:center}
.loc .map{position:absolute;left:6px;top:6px;width:223px;height:180px;background:linear-gradient(135deg,#eef0f2,#dfe6ec)}
.loc .name{position:absolute;left:8px;right:8px;top:196px;font-size:16.5px;line-height:30px;font-weight:300;color:var(--loc-text);text-transform:uppercase}
.loc .addr{position:absolute;left:8px;right:8px;top:260px;font-size:14px;line-height:30px;font-weight:300;color:#444}
/* footer */
.footer{left:0;top:3245px;width:1200px;height:445px;background:var(--footer)}
.badge{top:3300px;height:64px;background:rgba(255,255,255,.85);border-radius:4px}
.fcol h4{font-size:17px;font-weight:700;color:#fff;margin-bottom:14px}
.fcol a{display:block;font-size:15px;color:#fff;text-decoration:none;line-height:30px}
.contact-row{display:flex;gap:18px;font-size:15px;color:#fff;line-height:22px;align-items:flex-start}
.f-brand{left:848px;top:3470px;display:flex;align-items:center;gap:12px}
.f-brand .brand-dot{background:#fff}
.f-brand .brand-name{color:#fff;font-size:26px}
.f-soc{left:880px;top:3525px;display:flex;gap:12px}
.f-soc i{display:block;width:37px;height:37px;border:2px solid #fff;border-radius:50%}
.pay{left:882px;font-size:26px;color:#fff;font-weight:400;display:flex;align-items:center;gap:10px}
.pay b{display:block;width:22px;height:22px;background:#fff;border-radius:3px}
.bottom{left:0;top:3690px;width:1200px;height:64px;background:var(--footer-bar);color:#fff;font-size:14px;display:flex;align-items:center;justify-content:center}
</style>
</head>
<body>
<div class="page">

<header class="abs header">
  <div class="abs brand"><span class="brand-dot"></span><span class="brand-name">Corvale ENT Victoria</span></div>
  <div class="abs topbar">Call Now: 03 5550 1190 <span class="soc"></span><span class="sep">|</span><span class="soc"></span><span class="sep">|</span><span class="soc"></span><span class="sep">|</span><span class="soc"></span></div>
  <div class="abs btn-book">BOOK A CONSULTATION</div>
  <nav class="abs nav"><span>Our Team</span><span>Our Clinic</span><span>Children</span><span>Ear</span><span>Nose</span><span>Snoring &amp; Sleep</span><span>Voice</span><span>Head &amp; Neck</span><span>Facial Plastic</span><span>Patient Information</span></nav>
</header>

<section class="hero-wrap">
  <div class="abs hero" role="img" aria-label="Surgeon in green cap operating with a surgical microscope in theatre"></div>
  <div class="abs hero-shade"></div>
  <div class="hero">
    <h1 class="abs" style="left:109px;top:312px;font-size:33px;font-weight:500;color:#fff">EAR NOSE &amp; THROAT SURGEON</h1>
  </div>
  <p class="abs hero-sub">Our goal is to deliver gold standard<br>patient orientated care.</p>
  <div class="abs btn-pill hero-cta">CONTACT US</div>
  <div class="abs arrow" style="left:34px"><svg width="12" height="14" viewBox="0 0 12 14"><path d="M9 1 3 7l6 6" fill="none" stroke="#1f3a6e" stroke-width="2"/></svg></div>
  <div class="abs arrow" style="left:1129px"><svg width="12" height="14" viewBox="0 0 12 14"><path d="M3 1l6 6-6 6" fill="none" stroke="#1f3a6e" stroke-width="2"/></svg></div>
</section>

<div class="abs services-bg"></div>

<div class="abs feature f-book"><h3>BOOK AN APPOINTMENT</h3><div class="rule"></div><div class="btn-pill">LEARN MORE</div></div>
<div class="abs feature f-clinic"><h3>OUR CLINIC</h3><div class="rule"></div><div class="btn-pill">LEARN MORE</div></div>
<div class="abs feature f-team"><h3>OUR TEAM</h3><div class="rule"></div><div class="btn-pill">LEARN MORE</div></div>

<section class="services">
  <div class="abs tile" style="left:111px;top:926px"><div class="ph" role="img" aria-label="Doctor examining a young woman's neck" style="background:linear-gradient(135deg,#d8cfc9,#b89a8a)"></div><span>CHILDREN</span></div>
  <div class="abs tile" style="left:441px;top:926px"><div class="ph" role="img" aria-label="Woman blowing her nose into a tissue" style="background:linear-gradient(135deg,#e4e2e0,#b9b0aa)"></div><span>NOSE</span></div>
  <div class="abs tile" style="left:771px;top:926px"><div class="ph" role="img" aria-label="Doctors checking a patient's throat" style="background:linear-gradient(135deg,#cfdbe4,#a9b9c6)"></div><span>THROAT</span></div>
  <div class="abs tile" style="left:111px;top:1183px"><div class="ph" role="img" aria-label="Patient sleeping with a CPAP mask" style="background:linear-gradient(135deg,#e7e9ef,#b7bccb)"></div><span>SNORING &amp; SLEEP</span></div>
  <div class="abs tile" style="left:441px;top:1183px"><div class="ph" role="img" aria-label="Doctor consulting a patient in a clinic room" style="background:linear-gradient(135deg,#dfe2e6,#a7b2bf)"></div><span>VOICE</span></div>
  <div class="abs tile" style="left:771px;top:1183px"><div class="ph" role="img" aria-label="Hands massaging a patient's neck and shoulder" style="background:linear-gradient(135deg,#e8d3c7,#c7a08c)"></div><span>HEAD &amp; NECK</span></div>
</section>

<section class="about">
  <div class="abs about-photo" role="img" aria-label="Surgeon looking through a surgical microscope"></div>
  <svg class="abs" style="left:0;top:1524px" width="600" height="475" viewBox="0 0 600 475"><path d="M0 0H575C528 150 510 320 538 475H0Z" fill="#1f3a6e"/><path d="M575 0C528 150 510 320 538 475" fill="none" stroke="#982a78" stroke-width="3"/></svg>
  <h2 class="abs">CORVALE ENT VICTORIA</h2>
  <div class="abs rule"></div>
  <p class="abs">We want your experience with Corvale ENT Victoria to be a good one. To make things easier, please make sure you have the following with you.<br>Appointments can be made with Mr Daniel Marsh for Bendigo, Echuca, Melbourne, Mildura &amp; Shepparton by contacting us on 03 5550 1190. Alternatively our friendly receptionists will contact patients directly upon receiving referrals via fax, email or post.</p>
  <div class="abs btn-outline">LEARN MORE</div>
</section>

<section class="appointment">
  <h2 class="abs sec-title" style="top:2085px">YOUR FIRST APPOINTMENT</h2>
  <div class="abs sec-rule" style="top:2140px"></div>
  <p class="abs intro">We want your experience with Corvale ENT Victoria to be a good one. To make<br>things easier, please make sure you have the following with you.</p>
  <div class="abs need" style="left:113px"><div class="ring"><svg width="50" height="44" viewBox="0 0 50 44" fill="none" stroke="#982a78" stroke-width="2"><path d="M3 18 25 3l22 15v23H3Z"/><path d="M3 18l22 14 22-14"/><path d="M10 13V8h30v5"/></svg></div><p>Referral letter from<br>your GP</p></div>
  <div class="abs need" style="left:367px"><div class="ring"><svg width="44" height="50" viewBox="0 0 44 50" fill="none" stroke="#982a78" stroke-width="2"><path d="M22 3 40 9v15c0 12-8 20-18 23C12 44 4 36 4 24V9Z"/><path d="M17 16h10v6h6v10h-6v6H17v-6h-6V22h6Z"/></svg></div><p>Medicare Card or<br>private insurance<br>details</p></div>
  <div class="abs need" style="left:620px"><div class="ring"><svg width="52" height="46" viewBox="0 0 52 46" fill="none" stroke="#982a78" stroke-width="2"><rect x="3" y="3" width="46" height="30"/><path d="M20 33v8h12v-8M14 43h24M12 12h12M12 18h8M30 12h10v14H30Z"/></svg></div><p>Current test results, relevant doctors letters and physical copies of any imaging (X-ray etc)</p></div>
  <div class="abs need" style="left:873px"><div class="ring"><svg width="40" height="50" viewBox="0 0 40 50" fill="none" stroke="#982a78" stroke-width="2"><rect x="5" y="6" width="30" height="40" rx="2"/><path d="M14 3h12v6H14ZM12 20h16M12 27h16M12 34h10"/></svg></div><p>Current Medication<br>List</p></div>
</section>

<section class="locations">
  <div class="abs loc-bg" role="img" aria-label="Faded aerial view of a city skyline"></div>
  <h2 class="abs sec-title" style="top:2700px">OUR LOCATIONS</h2>
  <div class="abs sec-rule" style="top:2755px"></div>
  <div class="abs loc" style="left:112px"><div class="map" role="img" aria-label="Street map of the Echuca clinic"></div><div class="name">Riverside Specialist<br>Centre</div><div class="addr">15 Harbour Lane Echuca<br>Vic 3564</div></div>
  <div class="abs loc" style="left:360px"><div class="map" role="img" aria-label="Street map of the Bendigo rooms"></div><div class="name">Bendigo Consulting<br>Rooms</div><div class="addr">48 Ridgeway Street Bendigo<br>Vic 3550</div></div>
  <div class="abs loc" style="left:607px"><div class="map" role="img" aria-label="Street map of the Mildura clinic"></div><div class="name">Clearwave Hearing<br>Specialists Mildura</div><div class="addr">3/72 Orchard Avenue Mildura<br>VIC 3500</div></div>
  <div class="abs loc" style="left:854px"><div class="map" role="img" aria-label="Street map of the Melbourne clinic"></div><div class="name">Medical Specialists<br>on Keller</div><div class="addr">5, 310 Keller Street Melbourne<br>Vic 3000</div></div>
</section>

<footer>
  <div class="abs footer"></div>
  <div class="abs badge" style="left:120px;width:135px"></div>
  <div class="abs badge" style="left:312px;width:135px"></div>
  <div class="abs badge" style="left:505px;width:110px"></div>
  <div class="abs badge" style="left:670px;width:170px"></div>
  <div class="abs badge" style="left:895px;width:180px"></div>

  <div class="abs fcol" style="left:113px;top:3440px"><h4>QUICK LINKS</h4><a>Home</a><a>About</a><a>Our Clinic</a><a>Booking</a><a>ENT Conditions</a></div>
  <div class="abs fcol" style="left:309px;top:3440px"><h4>RESOURCES</h4><a>Facial Plastics</a><a>News &amp; Updates</a><a>Sitemap</a><a>Contact</a></div>
  <div class="abs fcol" style="left:477px;top:3440px"><h4>CONTACT US</h4>
    <div class="contact-row" style="margin-top:-2px"><svg width="12" height="16" viewBox="0 0 12 16" style="margin-top:5px"><path d="M6 1a5 5 0 0 1 5 5c0 4-5 9-5 9S1 10 1 6a5 5 0 0 1 5-5Z" fill="#fff"/><circle cx="6" cy="6" r="2" fill="#25304d"/></svg><span>48 Ridgeway Street Bendigo,<br>Victoria, 3550</span></div>
    <div class="contact-row" style="margin-top:12px"><svg width="13" height="10" viewBox="0 0 13 10" style="margin-top:6px"><rect width="13" height="10" fill="#fff"/><path d="M0 0l6.5 5L13 0" fill="none" stroke="#25304d"/></svg><span>admin@corvalepracticehub.com.au</span></div>
    <div class="contact-row" style="margin-top:20px"><svg width="13" height="13" viewBox="0 0 13 13" style="margin-top:4px"><path d="M3 0 5 3 3.5 5C4.5 7 6 8.5 8 9.5L10 8l3 2-1.5 3C6 12.5.5 7 0 1.5Z" fill="#fff"/></svg><span>03 5550 1190</span></div>
  </div>
  <div class="abs f-brand"><span class="brand-dot"></span><span class="brand-name">Corvale ENT Victoria</span></div>
  <div class="abs f-soc"><i></i><i></i><i></i><i></i></div>
  <div class="abs pay" style="top:3588px"><b></b>FlexiPay money</div>
  <div class="abs pay" style="top:3640px"><b></b>FlexiPay pay</div>
  <div class="abs bottom">© 2021 Corvale ENT Victoria. | All Rights Reserved</div>
</footer>

</div>
</body>
</html>
```